UPDATE: I have uploaded the selected logo from the other contest, please use it in your designs.

I have a logo design contest as well so not sure how PixelGuild handles that. They should integrate at some point. I will describe the overall theme with the logo description. See it for details.

The business card side of it would just build on that same theme.

Target Market(s)

8-40

Industry/Entity Type

Business

Contact Information for Business Card

FirstName LastName
Email

Logo Text

Velimor

Font styles to use
Sans Serif

Requirements
Must have
• the url Velimor.com somewhere in it.

```html
<!DOCTYPE html>
<html lang="en">
<head>
<meta charset="utf-8">
<title>Velimor Business Card</title>
<link href="https://fonts.googleapis.com/css2?family=Open+Sans:wght@400;600;700&display=swap" rel="stylesheet">
<style>
  :root {
    --stage: #1c1c1d;
    --card: #2b2929;
    --card-deep: #242222;
    --white: #f4f4f4;
    --orange: #f0961f;
    --muted: #d9d9d9;
  }
  * { box-sizing: border-box; margin: 0; padding: 0; }
  html, body {
    width: 1200px; height: 800px; overflow: hidden;
    background: var(--stage);
    font-family: "Open Sans", sans-serif;
  }
  .stage {
    position: relative; width: 1200px; height: 800px;
    display: flex; align-items: center; justify-content: center; gap: 60px;
  }
  .card {
    position: relative; width: 510px; height: 291px;
    background: linear-gradient(135deg, var(--card) 0%, var(--card-deep) 100%);
    overflow: hidden;
    box-shadow: 0 14px 30px rgba(0,0,0,.45);
  }
  /* front */
  .front-strip {
    position: absolute; top: 0; right: 0; width: 92px; height: 100%;
    background: var(--white);
  }
  .brand {
    position: absolute; color: var(--orange); font-weight: 600;
    letter-spacing: .02em; white-space: nowrap;
  }
  .front .brand { left: 209px; top: 122px; font-size: 34px; transform: translateX(-20%); }
  /* back */
  .identity { position: absolute; left: 40px; top: 78px; }
  .identity .name { font-size: 17px; font-weight: 700; color: var(--white); line-height: 1.1; }
  .identity .name .first { color: var(--orange); }
  .identity .role { font-size: 11px; color: var(--muted); margin-top: 2px; }
  .contact { position: absolute; left: 72px; top: 140px; list-style: none; }
  .contact li { font-size: 12px; color: var(--muted); line-height: 30px; }
  .divider {
    position: absolute; left: 262px; top: 36px; width: 3px; height: 182px;
    background: var(--white);
  }
  .back .brand { left: 300px; top: 100px; font-size: 30px; }
  .accent-band {
    position: absolute; left: 0; bottom: 0; width: 100%; height: 26px;
    background: var(--orange);
  }
</style>
</head>
<body>
  <main class="stage">
    <section class="card front" aria-label="Business card front">
      <span class="brand">Velimor</span>
      <div class="front-strip"></div>
    </section>

    <section class="card back" aria-label="Business card back">
      <div class="identity">
        <p class="name"><span class="first">Mara</span> Lind</p>
        <p class="role">Manager</p>
      </div>
      <ul class="contact">
        <li>Url:Velimor.com</li>
        <li>Phoon:00 987 654 321</li>
        <li>Email:maralind@velimor.com</li>
      </ul>
      <div class="divider"></div>
      <span class="brand">Velimor</span>
      <div class="accent-band"></div>
    </section>
  </main>
</body>
</html>
```